Flyer for annual KESTREL SUMMIT 2020

I would like a church event flyer designed. The event is called "KESTREL SUMMIT 2020". I am looking for a professional, yet catchy design that uses our brand colors and logo creatively while communicating key information of the event effectively.

1. The logo is attached in two color formats. The designer has the choice to use them as he/she want.

2. The location of the event is: Harlow Community Center, 239 Fennimore Street, Portland, ME 04117

3. Time and date of event. The designer can organize and format the date and time as he/she pleases.
Thursday December 31st @ 6:30PM
Friday January 1st @ 6:30PM
Saturday 2nd @ 6:30PM
Sunday 3rd @ 4:30PM

4. The topic of the event is "In Fire and On Fire". The designer is free to use this phrase as he/she pleases to create a good composition.

5. Speaker: Prophet Marcus Olunde (2 pictures of the speaker to choose from are attached)

6. Contact information: contact@brightmeadowfold.org - Telephone number: 207 583 2914

7. I would also like the following three words on the flyer. These words describe the focus of the event: FIRE, REVIVAL, PROPHETIC

Target Market(s)

Young adults

Font styles to use
Sans Serif

Requirements
Must have
• Logo, speaker's picture
Should not have
• cross image, church image

```html
<!DOCTYPE html>
<html lang="en">
<head>
<meta charset="utf-8">
<title>Kestrel Summit 2020 Flyer</title>
<link href="https://fonts.googleapis.com/css2?family=Montserrat:wght@500;600;700;800;900&display=swap" rel="stylesheet">
<style>
  :root {
    --navy: #1f3557;
    --orange: #f7941d;
    --orange-deep: #e8611a;
    --slate: #cfd6e0;
    --peach: #fde3c6;
    --white: #ffffff;
    --ink: #24324a;
  }
  * { margin: 0; padding: 0; box-sizing: border-box; }
  html, body { width: 863px; height: 1200px; overflow: hidden; background: var(--white); }
  body { font-family: "Montserrat", sans-serif; color: var(--navy); }
  .flyer { position: relative; width: 863px; height: 1200px; overflow: hidden; }
  .backdrop { position: absolute; inset: 0; }
  .speaker-photo { position: absolute; left: 565px; top: 40px; width: 275px; height: 620px;
    background: linear-gradient(170deg, #e3e6ea 0%, #d0d4d9 22%, #c0432a 48%, #8c2a1a 78%, #4a1a14 100%); }
  .brand { position: absolute; left: 42px; top: 44px; display: flex; align-items: center; gap: 12px; }
  .brand-dot { width: 22px; height: 22px; border-radius: 50%; background: var(--orange); }
  .brand-name { font-weight: 800; font-size: 44px; letter-spacing: 2px; color: var(--navy); }
  .title { position: absolute; left: 40px; top: 214px; }
  .title-main { font-weight: 900; font-size: 84px; line-height: 1; letter-spacing: 1px;
    background: linear-gradient(90deg, var(--orange-deep), var(--orange)); -webkit-background-clip: text; background-clip: text; color: transparent; }
  .title-sub { display: flex; align-items: baseline; gap: 14px; margin-top: 4px; margin-left: 6px; }
  .title-sub .word { font-weight: 800; font-size: 30px; letter-spacing: 2px; color: var(--navy); }
  .title-sub .year { font-weight: 900; font-size: 62px; color: var(--navy); line-height: 1; }
  .schedule { position: absolute; left: 40px; top: 418px; width: 270px; }
  .month { display: inline-block; background: var(--peach); color: var(--orange-deep); font-weight: 800; font-size: 27px; letter-spacing: 1px; padding: 3px 12px; }
  .session { font-weight: 800; font-size: 36px; color: var(--navy); line-height: 1.25; margin-left: 8px; white-space: nowrap; }
  .session .at { font-size: 18px; font-weight: 700; margin: 0 6px; }
  .session .hour { color: var(--orange-deep); }
  .session sup { font-size: 17px; color: var(--orange-deep); }
  .month-gap { margin-top: 24px; }
  .speaker { position: absolute; left: 340px; top: 392px; }
  .speaker-label { font-weight: 700; font-size: 20px; color: var(--navy); letter-spacing: 1px; }
  .speaker-name { display: inline-block; margin-top: 6px; background: var(--navy); color: var(--white); font-weight: 800; font-size: 22px; padding: 8px 18px; letter-spacing: 0.5px; white-space: nowrap; }
  .venue { position: absolute; left: 340px; top: 496px; display: flex; gap: 12px; }
  .venue-arrow { width: 28px; height: 68px; flex: none; }
  .venue-name { font-weight: 800; font-size: 24px; line-height: 1.1; color: var(--navy); }
  .venue-address { margin-top: 8px; font-weight: 600; font-size: 12px; line-height: 1.35; color: var(--ink); letter-spacing: 0.5px; }
  .theme { position: absolute; left: 590px; top: 676px; color: var(--white); }
  .theme-line { font-weight: 900; line-height: 0.95; }
  .theme-in { font-size: 70px; }
  .theme-fire { color: var(--orange); }
  .theme-and { font-size: 38px; margin: 6px 0; }
  .theme-arrow { position: absolute; left: 503px; top: 762px; width: 58px; height: 96px; }
  .focus { position: absolute; left: 0; right: 0; top: 930px; text-align: center; padding-left: 200px; color: var(--white); font-weight: 700; font-size: 28px; letter-spacing: 6px; }
  .contact { position: absolute; right: 44px; top: 1008px; text-align: right; }
  .contact-label { display: inline-block; background: var(--orange); color: var(--white); font-weight: 700; font-size: 14px; letter-spacing: 1px; padding: 6px 14px; }
  .contact-email { margin-top: 12px; font-weight: 800; font-size: 24px; color: var(--navy); }
  .contact-phone { margin-top: 8px; display: flex; justify-content: flex-end; align-items: center; gap: 10px; font-weight: 800; font-size: 30px; color: var(--navy); }
  .contact-phone svg { width: 24px; height: 24px; }
</style>
</head>
<body>
<main class="flyer">
  <svg class="backdrop" width="863" height="1200" viewBox="0 0 863 1200" aria-hidden="true">
    <rect width="863" height="1200" fill="var(--white)"/>
    <polygon points="0,0 480,0 0,430" fill="var(--slate)"/>
  </svg>

  <div class="speaker-photo" role="img" aria-label="Portrait of the speaker in a red suit and glasses"></div>

  <svg class="backdrop" width="863" height="1200" viewBox="0 0 863 1200" aria-hidden="true">
    <defs>
      <linearGradient id="handsTone" x1="0" y1="0" x2="1" y2="1">
        <stop offset="0" stop-color="#d9b79a"/>
        <stop offset="0.5" stop-color="#a7714f"/>
        <stop offset="1" stop-color="#4b3327"/>
      </linearGradient>
    </defs>
    <polygon points="0,770 863,590 863,990 0,990" fill="url(#handsTone)" role="img" aria-label="Photo of hands joined in prayer"/>
    <polygon points="0,760 46,752 0,960" fill="var(--orange)"/>
    <polygon points="330,830 863,620 863,860 450,930" fill="var(--navy)"/>
    <polygon points="0,990 863,990 863,1200 0,1200" fill="var(--white)"/>
  </svg>

  <header class="brand">
    <span class="brand-dot"></span>
    <span class="brand-name">HALVEN</span>
  </header>

  <section class="title">
    <div class="title-main">KESTREL</div>
    <div class="title-sub"><span class="word">SUMMIT</span><span class="year">2020</span></div>
  </section>

  <section class="schedule">
    <div class="month">DECEMBER</div>
    <div class="session">31<span class="at">AT</span><span class="hour">6</span><sup>:30</sup><span class="hour">PM</span></div>
    <div class="month month-gap">JANUARY</div>
    <div class="session">01<span class="at">AT</span><span class="hour">6</span><sup>:30</sup><span class="hour">PM</span></div>
    <div class="session">02<span class="at">AT</span><span class="hour">6</span><sup>:30</sup><span class="hour">PM</span></div>
    <div class="session">03<span class="at">AT</span><span class="hour">4</span><sup>:30</sup><span class="hour">PM</span></div>
  </section>

  <section class="speaker">
    <div class="speaker-label">SPEAKER:</div>
    <div class="speaker-name">PROPHET MARCUS OLUNDE</div>
  </section>

  <section class="venue">
    <svg class="venue-arrow" viewBox="0 0 28 68" aria-hidden="true"><polygon points="0,0 28,34 0,68" fill="var(--orange)"/></svg>
    <div>
      <div class="venue-name">HARLOW<br>COMMUNITY<br>CENTER</div>
      <div class="venue-address">239 FENNIMORE<br>STREET, PORTLAND,<br>ME 04117</div>
    </div>
  </section>

  <svg class="theme-arrow" viewBox="0 0 58 96" aria-hidden="true"><polygon points="0,0 58,48 0,96" fill="var(--orange)"/></svg>
  <section class="theme">
    <div class="theme-line theme-in">IN <span class="theme-fire">FIRE</span></div>
    <div class="theme-line theme-and">AND ON</div>
    <div class="theme-line theme-in theme-fire">FIRE</div>
  </section>

  <div class="focus">FIRE | REVIVAL | PROPHETIC</div>

  <section class="contact">
    <div class="contact-label">CONTACT INFORMATION</div>
    <div class="contact-email">CONTACT@BRIGHTMEADOWFOLD.ORG</div>
    <div class="contact-phone">
      <svg viewBox="0 0 24 24" aria-hidden="true"><path fill="var(--navy)" d="M6.6 10.8a15.1 15.1 0 0 0 6.6 6.6l2.2-2.2c.3-.3.7-.4 1-.2 1.1.4 2.3.6 3.6.6.6 0 1 .4 1 1V20c0 .6-.4 1-1 1A17 17 0 0 1 3 4c0-.6.4-1 1-1h3.5c.6 0 1 .4 1 1 0 1.3.2 2.5.6 3.6.1.3 0 .7-.2 1z"/></svg>
      <span>207 583 2914</span>
    </div>
  </section>
</main>
</body>
</html>
```